Willow of Meadow Uniform Label Redesign

To refine our current product label designs into one, simple, modern, crisp, general look that can be adapted to all our all Natural Skin Care and Wellness products. I am inspired by the elegant versatility of products like Lumavel Botanic Beauty or Tarn Beauty label schemes. We no longer want labels that indicate scent or ingredients. We have two primary colors that we want to maintain (#096CA3 and #DEE33F), and are willing to entertain subtle additions of others, other than black. Our labels will be printed on white or clear material. We use mainly Cosmo or Boston Round container shapes, plus flat top, smooth, round jars. Maybe a faded watermark highlight the "natural" or "beautiful" side of our products. we need to convey confidence, while remaining simple. We currently use the Advantage font. Maybe Century Gothic may work. Something similar that is easy on the eyes. Maybe vertical main text? We are willing to entertain a lot of ideas. These designs will offer ideas into our eventual Website (www.willowofmeadow-example.com) redesign.

Target Market(s)

Those who are familiar with the power of natural, plant based skin care and wellness products

Industry/Entity Type

Natural Skin Care and Wellness

Font styles to use
Sans Serif
Other font styles liked:
• Century Gothic, Advantage, or similar that is easy on the eyes

Colors
0054AA
0677BA
7BADD7
CADEEF
E8F1F8
59FF00
82FF00
B8FF75
E3FFCB
F4FFEA

Requirements
Must have
• "Clean Lines"; These colors: (#096CA3 and #DEE33F)
Nice to have
• MAYBE vertical main text or a watermark image

```html
<!DOCTYPE html>
<html lang="en">
<head>
<meta charset="utf-8">
<title>Willow of Meadow – Green Tea Hydrating Serum Label</title>
<link rel="stylesheet" href="https://fonts.googleapis.com/css2?family=Kreon:wght@400&family=Open+Sans:wght@400;700&display=swap">
<style>
  :root {
    --brand-blue: #096CA3;
    --band-blue: #1155A6;
    --brand-yellow: #DEE33F;
    --band-yellow: #DDE53A;
    --ink: #2b2b2b;
    --leaf-tone: #dfe9e6;
    --label-white: #ffffff;
    --backdrop: #d3d3d5;
  }
  * { margin: 0; padding: 0; box-sizing: border-box; }
  html, body { width: 1200px; height: 900px; overflow: hidden; }
  body {
    background: var(--backdrop);
    font-family: "Open Sans", Arial, sans-serif;
    color: var(--ink);
  }
  .label {
    position: absolute;
    left: 60px; top: 184px;
    width: 1080px; height: 532px;
    background: var(--label-white);
    overflow: hidden;
    box-shadow: 0 2px 6px rgba(0,0,0,0.18);
  }
  .band { position: absolute; left: 0; width: 100%; }
  .band--top { top: 0; height: 51px; background: var(--band-yellow); }
  .band--bottom { bottom: 0; height: 57px; background: linear-gradient(90deg, var(--band-blue), var(--brand-blue)); }

  .illustration { position: absolute; background: radial-gradient(ellipse at center, var(--leaf-tone), rgba(223,233,230,0.2) 75%, transparent); }
  .illustration--top-left { left: 69px; top: 51px; width: 371px; height: 126px; }
  .illustration--bottom-right { left: 540px; top: 309px; width: 355px; height: 166px; }

  .info-column { position: absolute; text-align: center; }
  .info-column--left { left: 61px; top: 186px; width: 220px; }
  .info-column--right { left: 790px; top: 80px; width: 240px; }
  .info-heading { font-weight: 700; font-size: 13px; letter-spacing: 0.08em; margin-bottom: 10px; }
  .info-text { font-size: 13px; line-height: 17.5px; letter-spacing: 0.05em; margin-bottom: 24px; }

  .brand { position: absolute; left: 390px; top: 52px; width: 300px; text-align: center; }
  .brand-mark {
    width: 84px; height: 84px; margin: 0 auto 6px;
    border: 2px solid var(--brand-yellow); border-radius: 50%;
  }
  .brand-name { font-family: "Kreon", Georgia, serif; font-size: 29px; line-height: 1; color: var(--brand-blue); }
  .brand-tagline { font-size: 9px; margin-top: 3px; color: var(--ink); }

  .product-name {
    position: absolute; left: 397px; top: 258px;
    font-family: "Kreon", Georgia, serif; font-size: 26px; line-height: 33px;
    color: var(--brand-blue);
    padding-bottom: 6px;
    border-bottom: 4px solid var(--brand-yellow);
  }
  .product-volume { position: absolute; left: 397px; top: 428px; font-size: 17px; letter-spacing: 0.06em; }

  .social-links { display: flex; justify-content: center; gap: 14px; margin: 4px 0 14px; }
  .social-dot { width: 26px; height: 26px; border-radius: 50%; background: var(--brand-yellow); }
  .website { font-size: 13px; letter-spacing: 0.06em; }
</style>
</head>
<body>
  <main class="label">
    <div class="band band--top" role="img" aria-label="Yellow band with a leaf vein pattern"></div>

    <div class="illustration illustration--top-left" role="img" aria-label="Hand-drawn green tea leaf sketches"></div>

    <section class="info-column info-column--left">
      <h2 class="info-heading">Ingredients:</h2>
      <p class="info-text">Lorem ipsum dolor sit<br>amet, consectetuer<br>adipiscing elit, sed diam<br>nonummy nibh euismod<br>tincidunt ut laoreet</p>
      <h2 class="info-heading">Lorem ipsum:</h2>
      <p class="info-text">Lorem ipsum dolor sit<br>amet, consectetuer<br>adipiscing elit, sed diam<br>nonummy nibh euismod<br>tincidunt ut laoreet</p>
    </section>

    <header class="brand">
      <div class="brand-mark"></div>
      <h1 class="brand-name">Willow of Meadow</h1>
      <p class="brand-tagline">Simple. Beautiful. Timeless</p>
    </header>

    <h2 class="product-name">Green tea<br>Hydrating Serum</h2>
    <p class="product-volume">2 fl. oz. (60ml)</p>

    <div class="illustration illustration--bottom-right" role="img" aria-label="Hand-drawn green tea branch with leaves"></div>

    <section class="info-column info-column--right">
      <h2 class="info-heading">How to use:</h2>
      <p class="info-text">Lorem ipsum dolor sit amet,<br>consectetuer adipiscing elit,<br>sed diam nonummy nibh<br>euismod tincidunt ut laoreet</p>
      <h2 class="info-heading">Follow us:</h2>
      <div class="social-links">
        <span class="social-dot"></span><span class="social-dot"></span><span class="social-dot"></span>
      </div>
      <p class="website">www.willowofmeadow-example.com</p>
    </section>

    <div class="band band--bottom" role="img" aria-label="Blue band with a leaf vein pattern"></div>
  </main>
</body>
</html>
```